Personal Business Card Design Project

I require a two sided personal business card design.

I am a 35 year old Angel Investor and I invest in various niche internet and F&B projects in China. I am Chinese Australian

One side should be in English and the other side should be in Chinese.

My English details are:

Cole Marsh
Angel Investor

China: +86 1390 274 5183
Hong Kong: +852 6133 4087
Email: cole@cdmarsh.net
Address: Flat 2407, Block 5, Pinecrest Gardens,
42 Maoyuan Road (near Beiling Road),
Shanghai, 200437,
China

My Chinese details are (do not print the text in brackets)

袁哲明 (Name)
天使投资者(Angel Investor)

中国 (China): +86 1390 274 5183
香港 (Hong Kong): +852 6133 4087
Email: cole@cdmarsh.net
地址 (Address): 上海市茂园路42号5号楼2407室
松岭花园, 中国 200437

Target Market(s)

I will only give this card to present to new partners and suppliers and people asking for funding. Not customers.

Industry/Entity Type

Internet

Requirements
Must have
• Something a little humourous in terms of graphics that suggest helping something to grow since I invest in startups. But I want a sophisticated look to it as well.
Nice to have
• Black and White tongue in cheek graphics but not overboard.

The whole card can be not conventional in shape or have cutouts but still retain the business standard business card size.

```html
<!DOCTYPE html>
<html lang="en">
<head>
<meta charset="utf-8">
<title>Cole Marsh – Business Card</title>
<link rel="stylesheet" href="https://fonts.googleapis.com/css2?family=Noto+Sans:wght@700&family=Noto+Sans+SC:wght@300;400&family=Fira+Sans:ital,wght@1,300&display=swap">
<style>
  :root{
    --bg:#ececec;
    --orange:#f5b041;
    --purple:#6a539c;
    --green:#56b04b;
    --leaf:#93c657;
    --ink:#111111;
    --paper:#ffffff;
  }
  html,body{margin:0;padding:0;overflow:hidden;}
  body{width:1200px;height:1000px;background:var(--bg);position:relative;}
  .card{
    position:absolute;width:691px;height:397px;overflow:hidden;
    box-shadow:6px 6px 6px rgba(0,0,0,.35);
  }
  .card--en{left:115px;top:68px;}
  .card--zh{left:394px;top:534px;}
  .card__art{position:absolute;inset:0;}
  .band{filter:drop-shadow(-4px 5px 5px rgba(0,0,0,.45));}
  .disc{filter:drop-shadow(-6px 4px 6px rgba(0,0,0,.45));}
  .text{position:absolute;margin:0;}
  .card--en .name{left:40px;top:40px;font:700 30px/1.1 "Noto Sans",sans-serif;color:var(--ink);}
  .card--en .role{left:40px;top:78px;font:700 20px/1.1 "Noto Sans",sans-serif;color:var(--ink);}
  .card--en .contact{left:35px;top:171px;font:700 19.5px/26px "Noto Sans",sans-serif;color:var(--paper);white-space:nowrap;}
  .card--zh .name{left:38px;top:48px;font:400 25px/1.2 "Noto Sans SC",sans-serif;color:var(--ink);}
  .card--zh .role{left:38px;top:85px;font:400 16px/1.2 "Noto Sans SC",sans-serif;color:var(--ink);}
  .card--zh .contact{left:38px;top:168px;font:300 18.5px/38px "Noto Sans SC",sans-serif;color:var(--paper);white-space:nowrap;}
  .latin{font-family:"Fira Sans",sans-serif;font-style:italic;font-weight:300;}
  .contact span{display:block;}
</style>
</head>
<body>

<section class="card card--en" lang="en">
  <svg class="card__art" viewBox="0 0 691 397" width="691" height="397">
    <defs>
      <clipPath id="disc-en"><circle cx="594" cy="198" r="226"/></clipPath>
      <linearGradient id="leaf-en" x1="0" y1="1" x2="1" y2="0">
        <stop offset="0" stop-color="var(--leaf)" stop-opacity=".55"/>
        <stop offset="1" stop-color="var(--leaf)" stop-opacity=".95"/>
      </linearGradient>
    </defs>
    <rect width="691" height="397" fill="var(--purple)"/>
    <polygon class="band" points="0,0 691,0 691,100 390,104 0,139" fill="var(--orange)"/>
    <circle class="disc" cx="594" cy="198" r="226" fill="var(--green)"/>
    <g clip-path="url(#disc-en)">
      <ellipse role="img" aria-label="Growing wing of leaves" cx="640" cy="220" rx="70" ry="190" transform="rotate(25 640 220)" fill="url(#leaf-en)"/>
    </g>
    <circle role="img" aria-label="Winking mascot badge" cx="334" cy="67" r="33" fill="var(--paper)"/>
  </svg>
  <h1 class="text name">Cole Marsh</h1>
  <p class="text role">Angel Investor</p>
  <p class="text contact">
    <span>China: +86 1390 274 5183</span>
    <span>Hong Kong: +852 6133 4087</span>
    <span>Email: cole@cdmarsh.net</span>
    <span>Address: Flat 2407, Block 5, Pinecrest Gardens,</span>
    <span>42 Maoyuan Road (near Beiling Road),</span>
    <span>Shanghai, 200437,</span>
    <span>China</span>
  </p>
</section>

<section class="card card--zh" lang="zh-Hans">
  <svg class="card__art" viewBox="0 0 691 397" width="691" height="397">
    <defs>
      <clipPath id="disc-zh"><circle cx="594" cy="198" r="226"/></clipPath>
      <linearGradient id="leaf-zh" x1="0" y1="1" x2="1" y2="0">
        <stop offset="0" stop-color="var(--leaf)" stop-opacity=".55"/>
        <stop offset="1" stop-color="var(--leaf)" stop-opacity=".95"/>
      </linearGradient>
    </defs>
    <rect width="691" height="397" fill="var(--purple)"/>
    <polygon class="band" points="0,0 691,0 691,100 386,106 0,139" fill="var(--orange)"/>
    <circle class="disc" cx="594" cy="198" r="226" fill="var(--green)"/>
    <g clip-path="url(#disc-zh)">
      <ellipse role="img" aria-label="Growing wing of leaves" cx="640" cy="220" rx="70" ry="190" transform="rotate(25 640 220)" fill="url(#leaf-zh)"/>
    </g>
    <circle role="img" aria-label="Winking mascot badge" cx="333" cy="65" r="33" fill="var(--paper)"/>
  </svg>
  <h1 class="text name">袁哲明</h1>
  <p class="text role">天使投资者</p>
  <p class="text contact">
    <span>中国: <span class="latin" style="display:inline">+86 1390 274 5183</span></span>
    <span>香港: <span class="latin" style="display:inline">+852 6133 4087</span></span>
    <span class="latin">Email: cole@cdmarsh.net</span>
    <span>地址: 上海市茂园路42号5号楼2407室</span>
    <span>松岭花园, 中国 <span class="latin" style="display:inline">200437</span></span>
  </p>
</section>

</body>
</html>
```